Double sided flyer for industrial investment firm

We need a A4 double sided flyer (1 page, see attached draft), which we will fold in the midle. Text is attached. What is missing is a professional and clean looking design. Text length can not be changed. it is all in German, but that should not influence the design. The flyer is added to a letter which we send to small industrial companies as an introduction to us as an investor.

What is important?
- No fancy, colorful and funny designs.
- We want a clean, professional almost minimalist design. it does not take much design elements.
- Format either landscape or vertical, whatever works best.
- stay with the colors of our company (grey, blue). see www.velmora-ag.ch for details.
- Currently used graphic in the document should be used, but is not a must. Otherwise stay with pictures or Swiss Alps (if more pictures are needed). will upload some pictures as examples.

Format for the finished flyer: InDesign and Word document or similar.
Updates

The flyer will be folded in the middle so that it becomes A5. all current designs work only as a A4 format. An A4 folded has basically 4 pages, each being A5 size. Please adapt the design accordingly.

Target Market(s)

Owners of small to medium industrial companies in Switzerland

Industry/Entity Type

Industrial

Font styles to use
Serif
Sans Serif

Colors
0255a3
3276b5
85abd2
cedeed

Requirements
Must have
• 1 page, double sided. folded in the middle. A4 Format

```html
<!DOCTYPE html>
<html lang="de">
<head>
<meta charset="utf-8">
<title>Velmora – Faltflyer</title>
<link href="https://fonts.googleapis.com/css2?family=PT+Sans:ital,wght@0,400;0,700;1,400&family=PT+Serif:wght@700&display=swap" rel="stylesheet">
<style>
  :root {
    --blue-deep: #0255a3;
    --blue-mid: #3276b5;
    --blue-light: #85abd2;
    --blue-pale: #cedeed;
    --navy-text: #1d4f8c;
    --paper: #ffffff;
    --stage: #e4e4e4;
    --fold: rgba(0, 0, 0, 0.08);
  }
  * { margin: 0; padding: 0; box-sizing: border-box; }
  html, body {
    width: 1200px; height: 1000px; overflow: hidden;
    background: var(--stage);
    font-family: "PT Sans", Arial, sans-serif;
  }
  .spread {
    position: absolute; left: 60px; top: 118px;
    width: 1080px; height: 764px;
    background: var(--paper);
    box-shadow: 0 6px 24px rgba(0,0,0,0.18);
    overflow: hidden;
  }
  .spread-art { position: absolute; inset: 0; }
  .fold-line {
    position: absolute; left: 539px; top: 0; width: 2px; height: 100%;
    background: var(--fold);
  }
  .back-url {
    position: absolute; left: 30px; top: 712px;
    color: var(--paper); font-weight: 700; font-size: 14px; letter-spacing: 1.5px;
    white-space: nowrap;
  }
  .back-brand {
    position: absolute; left: 284px; top: 620px;
    font-family: "PT Serif", Georgia, serif; font-weight: 700;
    font-size: 19px; color: var(--blue-deep); letter-spacing: 0.5px;
    white-space: nowrap;
  }
  .back-divider {
    position: absolute; left: 388px; top: 572px; width: 1px; height: 120px;
    background: var(--blue-deep);
  }
  .contact {
    position: absolute; left: 396px; top: 578px; width: 134px;
    text-align: right; font-style: italic; font-size: 13px; line-height: 1.4;
    color: var(--navy-text); list-style: none; white-space: nowrap;
  }
  .front-brand {
    position: absolute; left: 612px; top: 540px;
    display: flex; align-items: center; gap: 14px;
  }
  .brand-square { width: 28px; height: 28px; background: var(--blue-deep); }
  .brand-name {
    font-family: "PT Serif", Georgia, serif; font-weight: 700;
    font-size: 50px; line-height: 1; color: var(--blue-deep); letter-spacing: 1px;
  }
  .tagline {
    position: absolute; left: 656px; top: 600px;
    font-size: 15px; color: var(--navy-text);
  }
  .front-url {
    position: absolute; left: 690px; top: 700px;
    font-size: 14px; font-weight: 700; letter-spacing: 7px; color: var(--navy-text);
  }
</style>
</head>
<body>
  <main class="spread">
    <svg class="spread-art" width="1080" height="764" viewBox="0 0 1080 764">
      <defs>
        <linearGradient id="sky-blue" x1="0" y1="0" x2="0.3" y2="1">
          <stop offset="0" stop-color="#2b86b8"/>
          <stop offset="0.5" stop-color="#0255a3"/>
          <stop offset="1" stop-color="#0b4f8f"/>
        </linearGradient>
        <radialGradient id="globe-fill" cx="0.45" cy="0.45" r="0.6">
          <stop offset="0" stop-color="#eef2f6"/>
          <stop offset="0.6" stop-color="#a9b8c8"/>
          <stop offset="1" stop-color="#5f7386"/>
        </radialGradient>
        <radialGradient id="globe-shadow" cx="0.5" cy="0.5" r="0.5">
          <stop offset="0" stop-color="rgba(0,0,0,0.35)"/>
          <stop offset="1" stop-color="rgba(0,0,0,0)"/>
        </radialGradient>
      </defs>
      <rect class="blue-field" width="1080" height="764" fill="url(#sky-blue)"/>
      <path class="white-dome" d="M230,764 C320,480 470,330 650,330 C850,330 1000,430 1080,580 L1080,764 Z" fill="#ffffff"/>
      <ellipse class="globe-shadow" cx="870" cy="505" rx="120" ry="26" fill="url(#globe-shadow)"/>
      <circle class="globe-photo" cx="860" cy="385" r="120" fill="url(#globe-fill)" role="img" aria-label="Glaskugel mit verschneitem Alpengipfel"/>
    </svg>
    <div class="fold-line"></div>

    <section class="panel-back">
      <p class="back-url">www.velmora-ag.ch</p>
      <p class="back-brand">VELMORA</p>
      <div class="back-divider"></div>
      <ul class="contact">
        <li>Seefeldstrasse 42</li>
        <li>8008 Zürich</li>
        <li>Telefon: 044 210 55 80</li>
        <li>info@velmora-ag.ch</li>
        <li>www.velmora-ag.ch</li>
      </ul>
    </section>

    <section class="panel-front">
      <div class="front-brand">
        <span class="brand-square"></span>
        <h1 class="brand-name">VELMORA</h1>
      </div>
      <p class="tagline">Fragen und Antworten zu Velmora</p>
      <p class="front-url">www.velmora-ag.ch</p>
    </section>
  </main>
</body>
</html>
```